Powerpoint template
Zielgruppe
Scientific research, novel molecule discovery & development”
Aufgabenstellung
Design of a template in the 16:9 aspect ratio - this will be used to create an interactive pdf employing indesign creative software.
The template should include options for opening slides , transition slides , and also closing slides.
Overall the design should be 'clean , neat and with lots of white space' - here the website of a similar company to ours which represents a direction in terms of design that approximates what we would like our final interactive pdf to look like. https://torvexlab.co/
As guidance please refer to the enclosed document with 3 design options that were created by a freelance designer working with the company-the first example is probably the closest to what we would like but we are not exactly satisfied with this example. The black lettering also is too dominant and not appropriate.
The last option is very much 'business focused' and such a design could be considered if the theme is more scientific rather than business orientated. The second example we consider inappropriate and too 'traditional' and not modern enough at all.

```html
<!DOCTYPE html>
<html lang="en">
<head>
<meta charset="utf-8">
<title>Velacor Therapeutics – Slide Template</title>
<link href="https://fonts.googleapis.com/css2?family=Heebo:wght@400;500;700&display=swap" rel="stylesheet">
<style>
:root{
  --page:#dfe3e8;
  --navy:#0e2262;
  --navy-mid:#12306f;
  --teal:#166079;
  --panel:#0f2a6c;
  --yellow:#f9d232;
  --white:#ffffff;
  --muted:#c7d2ea;
  --stat:#1a5685;
}
*{margin:0;padding:0;box-sizing:border-box}
html,body{width:846px;height:1200px;overflow:hidden;background:var(--page)}
body{font-family:'Heebo',Arial,sans-serif;color:var(--white)}
.deck{position:absolute;left:20px;top:253px;display:grid;grid-template-columns:397px 397px;grid-auto-rows:223px;gap:12px}
.slide{position:relative;overflow:hidden;background:linear-gradient(135deg,var(--navy) 0%,var(--navy-mid) 55%,var(--teal) 100%);box-shadow:0 2px 6px rgba(20,30,60,.18)}
.wave{position:absolute;inset:0;background:radial-gradient(ellipse 70% 22% at 45% 58%,rgba(110,120,220,.28),transparent 70%),radial-gradient(ellipse 60% 18% at 75% 48%,rgba(80,140,210,.18),transparent 70%)}
.abs{position:absolute}
.brand{position:absolute;display:flex;align-items:center;gap:4px;font-weight:500;line-height:.95;text-transform:uppercase}
.brand .dot{border-radius:50%;background:var(--white);opacity:.9}
.brand-sm{left:14px;top:12px;font-size:6px}
.brand-sm .dot{width:10px;height:10px}
.brand-lg{left:69px;top:33px;font-size:12.5px;gap:7px}
.brand-lg .dot{width:26px;height:26px}
.footer-url{position:absolute;left:12px;bottom:11px;font-size:3px;color:var(--muted)}
.footer-url b{color:var(--white)}
.page-no{position:absolute;right:16px;bottom:11px;font-size:3px;color:var(--muted)}
.yellow{color:var(--yellow)}
.pill{position:absolute;background:var(--yellow);color:var(--navy);border-radius:8px;font-weight:700;display:flex;align-items:center;justify-content:center;gap:4px}
.pill .tri{width:0;height:0;border-left:3px solid var(--navy);border-top:2px solid transparent;border-bottom:2px solid transparent}
.rule{position:absolute;height:1px;background:var(--white)}
/* opening */
.hero-title{left:69px;top:92px;font-size:10.5px;font-weight:700;line-height:1.3;color:var(--yellow)}
.hero-body{left:69px;top:150px;font-size:3.8px;line-height:1.8;color:var(--white);width:215px}
/* toc */
.toc-title{left:70px;top:106px;text-align:right;width:58px;font-size:9px;line-height:1.05}
.toc-title span{display:block;font-size:14px;font-weight:700;color:var(--yellow)}
.toc-item{position:absolute;left:161px;width:220px;font-size:3.7px;color:var(--white)}
.toc-item h4{font-size:6px;font-weight:700;color:var(--yellow);margin-bottom:2px;position:relative}
.toc-item h4::before{content:"";position:absolute;left:-8px;top:2.5px;width:1.5px;height:1.5px;border-radius:50%;background:var(--yellow)}
.toc-item .line{position:absolute;left:133px;top:11px;width:24px;height:.5px;background:var(--muted)}
.toc-item .num{position:absolute;left:162px;top:6px;font-size:8px;font-weight:400;color:transparent;-webkit-text-stroke:.4px var(--white)}
/* strength / journey */
.col{position:absolute;top:68px;width:125px}
.col h2{font-size:16px;font-weight:700;color:var(--yellow);line-height:1.2}
.col .bar{width:28px;height:1px;background:var(--white);margin:6px 0 9px}
.col p{font-size:3.9px;line-height:1.9}
.col ul{list-style:none;margin-top:5px}
.col li{position:relative;padding-left:22px;font-size:3.9px;line-height:1.9;margin-bottom:5px}
.col li::before{content:"";position:absolute;left:6px;top:1px;width:6px;height:6px;border-radius:50%;background:var(--yellow)}
.col li::after{content:"";position:absolute;left:8.4px;top:2.6px;border-left:2px solid var(--navy);border-top:1.4px solid transparent;border-bottom:1.4px solid transparent}
/* facts */
.fact-box{position:absolute;left:172px;top:26px;width:169px;height:171px;border:.6px solid rgba(249,210,50,.7);border-radius:4px}
.fact{position:absolute;left:14px;width:150px;display:flex;gap:12px;align-items:flex-start}
.fact .icon{flex:none;width:22px;height:24px;border-radius:3px;background:linear-gradient(135deg,rgba(249,210,50,.35),rgba(249,210,50,.12))}
.fact p{font-size:3.5px;line-height:1.6;text-align:justify}
.fact p i{font-style:italic}
/* stats */
.stat{position:absolute;width:96px;height:96px;background:var(--white);color:var(--stat);text-align:center}
.stat-a{left:95px;top:91px;border-radius:50% 0 50% 50%}
.stat-b{left:206px;top:46px;border-radius:50% 50% 50% 0}
.stat .big{font-size:18px;font-weight:700;line-height:1;margin-top:20px}
.stat .unit{font-size:5.5px;font-weight:700}
.stat .sep{width:58px;height:.5px;background:#b8c2cf;margin:6px auto 5px}
.stat .cap{font-size:3.6px;line-height:1.6;color:#5b6878}
/* contact */
.contact-card{position:absolute;left:64px;top:28px;width:267px;height:167px;background:var(--panel)}
.contact-card .dash{position:absolute;left:21px;top:18px;width:20px;height:1.5px;background:var(--yellow)}
.contact-card h2{position:absolute;left:21px;top:28px;font-size:13.5px;font-weight:700;line-height:1.3}
.label{position:absolute;font-size:4.6px;font-weight:700;letter-spacing:.3px}
.small{position:absolute;font-size:4px;line-height:1.95;color:var(--muted)}
.divider{position:absolute;left:148px;top:86px;width:.6px;height:46px;background:var(--muted)}
.cta{position:absolute;left:24px;top:139px;font-size:6px;font-weight:700;color:var(--yellow)}
svg.ico{position:absolute;fill:none;stroke:var(--yellow);stroke-width:1}
</style>
</head>
<body>
<main class="deck">

  <!-- opening slide -->
  <section class="slide">
    <div class="wave" role="img" aria-label="Soft flowing line-wave background pattern in violet and blue"></div>
    <div class="brand brand-lg"><span class="dot"></span><span>Velacor<br>Therapeutics</span></div>
    <h1 class="abs hero-title">A global leader in pioneering<br>research, novel molecule discovery<br>&amp; development</h1>
    <div class="rule" style="left:69px;top:143px;width:30px"></div>
    <p class="abs hero-body">Setting the standard through collaborative development, applied research and superlative in-house experience in extraction and characterization of natural psilocybin for disease modifying mental health treatments.</p>
    <div class="pill" style="left:69px;top:182px;width:40px;height:10px;font-size:4.8px;font-weight:500;letter-spacing:1px">2022</div>
  </section>

  <!-- table of contents -->
  <section class="slide">
    <div class="wave" role="img" aria-label="Soft flowing line-wave background pattern in violet and blue"></div>
    <div class="brand brand-sm"><span class="dot"></span><span>Velacor<br>Therapeutics</span></div>
    <h2 class="abs toc-title">Table of <span>Content</span></h2>
    <div class="toc-item" style="top:52px"><h4>Title Goes Here</h4>Lorem ipsum dolor sit amet, consectetur adipiscing elit.<span class="line"></span><span class="num">01</span></div>
    <div class="toc-item" style="top:82px"><h4>Title Goes Here</h4>Lorem ipsum dolor sit amet, consectetur adipiscing elit.<span class="line"></span><span class="num">02</span></div>
    <div class="toc-item" style="top:113px"><h4>Title Goes Here</h4>Lorem ipsum dolor sit amet, consectetur adipiscing elit.<span class="line"></span><span class="num">03</span></div>
    <div class="toc-item" style="top:143px"><h4>Title Goes Here</h4>Lorem ipsum dolor sit amet, consectetur adipiscing elit.<span class="line"></span><span class="num">04</span></div>
    <div class="toc-item" style="top:173px"><h4>Title Goes Here</h4>Lorem ipsum dolor sit amet, consectetur adipiscing elit.<span class="line"></span><span class="num">05</span></div>
    <div class="footer-url">www.<b>velacortherapeutics</b>.com</div>
    <div class="page-no">Page | 2</div>
  </section>

  <!-- strength / journey -->
  <section class="slide">
    <div class="wave" role="img" aria-label="Soft flowing line-wave background pattern in violet and blue"></div>
    <div class="brand brand-sm"><span class="dot"></span><span>Velacor<br>Therapeutics</span></div>
    <div class="col" style="left:52px">
      <h2>Our Strength</h2><div class="bar"></div>
      <p>We are led by a highly experienced board of directors that are pioneers in the industry Supported by an advisory board whose members are globally recognized. Collaborating with a Network of expertise in research &amp; development in Biopharma</p>
      <ul><li>Harwick College London</li><li>Ondara Research Center Brazil</li></ul>
    </div>
    <div class="col" style="left:221px">
      <h2>Our Journey</h2><div class="bar"></div>
      <p>Velacor Therapeutics's board of director's journey in psychedelics is characterized by an extensive and successful history in</p>
      <ul><li>Taking the lead from nature and in developing Therapeutics of Natural Origin</li><li>Development and harnessing of tryptamine compounds</li></ul>
    </div>
    <div class="footer-url">www.<b>velacortherapeutics</b>.com</div>
    <div class="page-no">Page | 3</div>
  </section>

  <!-- problem facts -->
  <section class="slide">
    <div class="wave" role="img" aria-label="Soft flowing line-wave background pattern in violet and blue"></div>
    <div class="brand brand-sm"><span class="dot"></span><span>Velacor<br>Therapeutics</span></div>
    <div class="pill" style="left:44px;top:105px;width:103px;height:13px;font-size:5.6px"><span class="tri"></span>Problem: clinical depression</div>
    <div class="fact-box">
      <div class="fact" style="top:12px"><span class="icon" role="img" aria-label="Line icon of a person sitting at a desk"></span><p>Major depressive disorder affects approximately 17.3 million American adults, or about 7.1% of the U.S. population age 18 and older, in a given year. <i>(Northfield Mental Health Institute "Major Depression", 2017)</i></p></div>
      <div class="fact" style="top:54px"><span class="icon" role="img" aria-label="Line icon of a human heart"></span><p>Adults with a depressive disorder or symptoms have a 64 percent greater risk of developing coronary artery disease. <i>(Northfield Health Institute, Heart disease and depression: A two-way relationship, 2017)</i></p></div>
      <div class="fact" style="top:97px"><span class="icon" role="img" aria-label="Line icon of a child"></span><p>1.9 million children, 3 – 17, have diagnosed depression. <i>(Halden Center for Disease Studies "Data and Statistics on Children's Mental Health", 2018)</i></p></div>
      <div class="fact" style="top:135px"><span class="icon" role="img" aria-label="Line icon of a head in profile with a medical cross"></span><p>Major depressive disorder is more prevalent in women than in men. <i>(Journal of Clinical Mind Research, 2003; Jun 18; 289(23): 3095-105)</i></p></div>
    </div>
    <div class="footer-url">www.<b>velacortherapeutics</b>.com</div>
    <div class="page-no">Page | 4</div>
  </section>

  <!-- stats -->
  <section class="slide">
    <div class="wave" role="img" aria-label="Soft flowing line-wave background pattern in violet and blue"></div>
    <div class="brand brand-sm"><span class="dot"></span><span>Velacor<br>Therapeutics</span></div>
    <div class="pill" style="left:94px;top:64px;width:104px;height:13px;font-size:5.6px"><span class="tri"></span>Problem: clinical depression</div>
    <div class="stat stat-b"><div class="big">$4</div><div class="unit">Billion</div><div class="sep"></div><div class="cap">$4 Billion<br>Global Annual Spend on Treatment<br>of Clinical Depression</div></div>
    <div class="stat stat-a"><div class="big">264</div><div class="unit">Million</div><div class="sep"></div><div class="cap">264+ Million<br>People Globally Suffering from<br>Clinical Depression</div></div>
    <div class="footer-url">www.<b>velacortherapeutics</b>.com</div>
    <div class="page-no">Page | 5</div>
  </section>

  <!-- closing -->
  <section class="slide">
    <div class="wave" role="img" aria-label="Soft flowing line-wave background pattern in violet and blue"></div>
    <div class="contact-card">
      <span class="dash"></span>
      <h2>Get in touch &amp; let us<br>know how we can help.</h2>
      <svg class="ico" style="left:22px;top:90px" width="14" height="16" viewBox="0 0 14 16"><path d="M7 13s-5-4.5-5-8a5 5 0 0 1 10 0c0 3.5-5 8-5 8z"/><circle cx="7" cy="5" r="1.8"/><path d="M9 14h4M2 15h3" stroke-dasharray="1 1"/></svg>
      <div class="label" style="left:47px;top:85px">ADDRESS</div>
      <div class="small" style="left:47px;top:94px;width:95px">Lorem ipsum dolor sit amet consectr adiscing quisque isno aliquet nuncas felis ullam corper vitaelis facilisis.</div>
      <span class="divider"></span>
      <svg class="ico" style="left:164px;top:84px" width="12" height="12" viewBox="0 0 12 12"><path d="M2 1.5l2 0 1 3-1.3 1a6 6 0 0 0 2.8 2.8l1-1.3 3 1v2A1.5 1.5 0 0 1 9 11.5 8.5 8.5 0 0 1 .5 3 1.5 1.5 0 0 1 2 1.5z"/></svg>
      <div class="label" style="left:186px;top:83px">PHONE</div>
      <div class="small" style="left:186px;top:90px">+62 8120 4455 3106</div>
      <svg class="ico" style="left:164px;top:107px" width="13" height="10" viewBox="0 0 13 10"><rect x=".5" y="1.5" width="10" height="7"/><path d="M.5 1.5l5 4 5-4"/></svg>
      <div class="label" style="left:186px;top:106px">EMAIL</div>
      <div class="small" style="left:186px;top:113px">example@yourdomain.com</div>
      <div class="cta">Contact Us Today</div>
    </div>
  </section>

</main>
</body>
</html>
```